" Assessoria e consultoria de projetos agropecuários com foco em bovinos. DIFERENCIAIS ? Atendimento personalizado; ? Foco em processos; Melhoria continua - metodologia LEAN ? Foco no cliente e na qualidade do serviço; ? Acompanhamento dos resultados gerados pela consultoria; ? Serviço com conhecimento agregado. Atendimento personalizado: A Brota enxerga a necessidade do contato personalizado com o cliente, demonstrando constantemente que a empresa está interessada em ajudá-lo e trazer soluções para seus problemas. ? Foco em processos: Como a maioria das empresas que prestam consultoria na área estão mais voltadas para TÉCNICAS animal, o foco em processos e gestao por processos torna-se um diferencial da Brota. A empresa poderia aproveitar essa vantagem divulgando a importância do gerenciamento eficaz nas fazendas através dos processos agropecuários. ? Foco no cliente e na qualidade do serviço: Através do atendimento personalizado, o consultor da Brota tem a responsabilidade de manter o comprometimento com o cliente e com a qualidade dos serviços entregues. Assim, a empresa cria uma boa relação com os consumidores, fidelizando-os. ? Acompanhamento dos resultados gerados pela consultoria: Além de prestar consultoria, a Empresa auxilia o cliente a implementar as técnicas e soluções, fazendo o acompanhamento de resultados com indicadores. ? Serviço com maior valor agregado: Através da constante busca por conhecimento na área, a qualidade dos projetos entregues será cada vez maior, consequentemente tornando-os mais eficazes e eficientes. "

```html
<!DOCTYPE html>
<html lang="pt-BR">
<head>
<meta charset="utf-8">
<title>Brota — Pasta institucional</title>
<link href="https://fonts.googleapis.com/css2?family=Montserrat:wght@400;500;600&display=swap" rel="stylesheet">
<style>
  :root {
    --stage: #e9ebee;
    --navy: #142848;
    --navy-deep: #0e1d36;
    --paper: #ffffff;
    --green: #3fa653;
    --green-light: #8fd19a;
    --grey-text: #8a9098;
    --white-text: #e8edf3;
  }
  * { box-sizing: border-box; margin: 0; padding: 0; }
  html, body { width: 1200px; height: 1200px; overflow: hidden; }
  body {
    background: var(--stage);
    font-family: "Montserrat", sans-serif;
    display: flex; align-items: center; justify-content: center;
  }
  .folder-spread {
    display: flex;
    width: 1000px; height: 700px;
    box-shadow: 0 12px 40px rgba(0,0,0,.18);
  }
  .panel { position: relative; width: 500px; height: 700px; overflow: hidden; }
  .panel-back { background: linear-gradient(160deg, var(--navy) 0%, var(--navy-deep) 100%); }
  .panel-front { background: var(--paper); }
  .top-band {
    position: absolute; top: 0; left: 0; right: 0; height: 22px;
    background: linear-gradient(180deg, var(--green-light) 0%, var(--green) 55%, #2d7f3e 100%);
  }
  .panel-front .top-band { height: 10px; }
  .brand {
    position: absolute; left: 0; right: 0;
    display: flex; align-items: center; justify-content: center; gap: 14px;
    font-weight: 500; letter-spacing: 0.32em; text-transform: uppercase;
  }
  .brand-dot { width: 18px; height: 18px; border-radius: 50%; background: var(--green); }
  .panel-back .brand { top: 330px; font-size: 30px; color: var(--white-text); }
  .panel-front .brand { top: 300px; font-size: 46px; color: var(--grey-text); }
  .tagline {
    position: absolute; top: 368px; left: 0; right: 0; text-align: center;
    font-size: 11px; letter-spacing: 0.4em; text-transform: uppercase; color: var(--green);
  }
  .contact {
    position: absolute; bottom: 46px; left: 70px; right: 70px;
    display: grid; grid-template-columns: 1fr 1fr; gap: 8px 20px;
    font-size: 11px; color: var(--white-text);
  }
  .contact-item { display: flex; align-items: center; gap: 7px; }
  .contact-item svg { width: 12px; height: 12px; flex: none; }
  .contact-item.wide { grid-column: 1 / -1; }
</style>
</head>
<body>
  <main class="folder-spread">
    <section class="panel panel-back">
      <div class="top-band"></div>
      <div class="brand"><span class="brand-dot"></span>Brota</div>
      <ul class="contact">
        <li class="contact-item">
          <svg viewBox="0 0 24 24" fill="#e8edf3"><path d="M6.6 10.8a15 15 0 0 0 6.6 6.6l2.2-2.2c.3-.3.7-.4 1-.2 1.1.4 2.3.6 3.6.6.6 0 1 .4 1 1V20c0 .6-.4 1-1 1A17 17 0 0 1 3 4c0-.6.4-1 1-1h3.5c.6 0 1 .4 1 1 0 1.3.2 2.5.6 3.6.1.3 0 .7-.2 1z"/></svg>
          +55 27 3000-1000
        </li>
        <li class="contact-item">
          <svg viewBox="0 0 24 24" fill="#e8edf3"><path d="M6.6 10.8a15 15 0 0 0 6.6 6.6l2.2-2.2c.3-.3.7-.4 1-.2 1.1.4 2.3.6 3.6.6.6 0 1 .4 1 1V20c0 .6-.4 1-1 1A17 17 0 0 1 3 4c0-.6.4-1 1-1h3.5c.6 0 1 .4 1 1 0 1.3.2 2.5.6 3.6.1.3 0 .7-.2 1z"/></svg>
          +55 27 9000-2000
        </li>
        <li class="contact-item">
          <svg viewBox="0 0 24 24" fill="none" stroke="#e8edf3" stroke-width="2"><rect x="3" y="5" width="18" height="14" rx="1"/><path d="M3 6l9 7 9-7"/></svg>
          contato@brota.com.br
        </li>
        <li class="contact-item">
          <svg viewBox="0 0 24 24" fill="none" stroke="#e8edf3" stroke-width="2"><circle cx="12" cy="12" r="9"/><path d="M3 12h18M12 3c3 3 3 15 0 18M12 3c-3 3-3 15 0 18"/></svg>
          www.brota.com.br
        </li>
        <li class="contact-item wide">
          <svg viewBox="0 0 24 24" fill="#e8edf3"><path d="M12 2a7 7 0 0 0-7 7c0 5 7 13 7 13s7-8 7-13a7 7 0 0 0-7-7zm0 9.5A2.5 2.5 0 1 1 12 6.5a2.5 2.5 0 0 1 0 5z"/></svg>
          Centro, Vitória - ES
        </li>
      </ul>
    </section>
    <section class="panel panel-front">
      <div class="top-band"></div>
      <div class="brand"><span class="brand-dot"></span>Brota</div>
      <p class="tagline">Processos Agropecuários</p>
    </section>
  </main>
</body>
</html>
```